Consulting firm needs a professional letterhead design

We need a professional letterhead design which is simple but unique. It should carry attributes of the latest designs in the market suitable for professional environmental consultancies.

- The logo is attached for you to USE.
- Our preferred color scheme is that shown in the logo.
- Letterhead text color is your choice to make.
- Logo to the left and text to the right plus slogan/tagline is desirable for this letterhead.

Use any address etc. of your choice in the letterhead.

Target Market(s)

Consulting firms and government agencies

Industry/Entity Type

Environmental Consultant

Colors
acd037
fece3e
85cae6
3277b5

Requirements
Must have
• Logo supplied and color scheme must be used.
Nice to have
• Nexa font is used in the Logo, so it would ne nice to have nexa font in the letterhead too.

```html
<!DOCTYPE html>
<html lang="en">
<head>
<meta charset="utf-8">
<title>Verdalyn Letterhead</title>
<link rel="stylesheet" href="https://fonts.googleapis.com/css2?family=Arimo:wght@400;700&family=Allura&display=swap">
<style>
  :root {
    --accent: #f6a21c;
    --ink: #4a4a4a;
    --brand: #2f5f9a;
    --tagline: #3277b5;
    --slogan: #8a8a8a;
    --paper: #ffffff;
  }
  * { margin: 0; padding: 0; box-sizing: border-box; }
  html, body { width: 857px; height: 1200px; overflow: hidden; background: var(--paper); }
  .letterhead {
    position: relative; width: 857px; height: 1200px;
    font-family: "Arimo", Arial, sans-serif; color: var(--ink);
  }
  .band { position: absolute; background: var(--accent); height: 12px; }
  .band--top-left { top: 0; left: 0; width: 366px; }
  .band--top-right { top: 0; left: 608px; width: 249px; }
  .band--bottom-left { bottom: 0; left: 0; width: 366px; }
  .band--bottom-right { bottom: 0; left: 608px; width: 249px; }

  .brand { position: absolute; left: 86px; top: 128px; display: flex; align-items: center; gap: 12px; }
  .brand__mark { width: 44px; height: 44px; border-radius: 50%; background: var(--brand); }
  .brand__name { font-weight: 700; font-size: 30px; color: var(--brand); letter-spacing: 1px; line-height: 1; }
  .brand__tagline { font-size: 10px; color: var(--tagline); margin-top: 3px; }

  .slogan {
    position: absolute; left: 500px; top: 140px;
    font-family: "Allura", cursive; font-size: 44px; color: var(--slogan);
  }

  .body { position: absolute; left: 86px; top: 326px; width: 690px; font-size: 11.5px; line-height: 1.45; }
  .body p { margin-bottom: 14px; }
  .date { margin-bottom: 16px !important; }
  .greeting { margin-bottom: 12px !important; }
  .closing { margin-top: 16px; margin-bottom: 38px !important; }

  .footer { position: absolute; top: 1050px; left: 86px; right: 60px; display: flex; font-size: 11px; }
  .footer__item { display: flex; align-items: center; gap: 10px; width: 300px; }
  .footer__item:nth-child(2) { width: 230px; }
  .footer__icon { width: 24px; height: 24px; border-radius: 50%; background: var(--accent); display: flex; align-items: center; justify-content: center; }
</style>
</head>
<body>
<div class="letterhead">
  <div class="band band--top-left"></div>
  <div class="band band--top-right"></div>

  <header class="brand">
    <div class="brand__mark"></div>
    <div>
      <div class="brand__name">VERDALYN</div>
      <div class="brand__tagline">Clear data for greener choices</div>
    </div>
  </header>
  <div class="slogan">your slogan here</div>

  <main class="body">
    <p class="date">August 28, 2011</p>
    <p>First Last Name<br>Street Address<br>City, State 00000</p>
    <p class="greeting">Dear :</p>
    <p>Lorem ipsum dolor sit amet, consectetur adipiscing elit. Aenean ut ipsum eget massa hendrerit vestibulum vel in velit. Donec pretium neque velit.</p>
    <p>Aliquam porta lectus nec mauris ornare venenatis. Vivamus non est turpis, at cursus sem. Mauris vehicula erat in diam auctor at bibendum nisi lacinia.</p>
    <p>Morbi imperdiet neque vehicula nunc convallis gravida. Vestibulum iaculis pretium placerat. Integer consequat, est sit amet facilisis eleifend, nibh nibh varius orci, eget dapibus arcu dui non purus. Pellentesque in magna mauris. Duis enim sapien, dictum vitae condimentum a, pulvinar vel lacus. Mauris et molestie nibh. Vestibulum vitae nulla at metus elementum porta sit amet interdum elit. Nulla sollicitudin neque eu nulla volutpat congue.</p>
    <p>Etiam pellentesque, velit id dapibus fermentum, turpis sapien ornare dui, ac tincidunt ligula odio congue purus. Nunc sed ante dui, in porta lectus. Cras nec sem lorem. In hac habitasse platea dictumst. Maecenas id diam quis dui porta tristique. Sed id egestas felis. Donec ullamcorper mattis posuere. Phasellus fermentum eleifend tortor vel dapibus. Vestibulum ante ipsum.</p>
    <p class="closing">Sincerely,</p>
    <p>Daniel Whitmore<br>NorthfieldGroup.com<br>P.O. Box 482190<br>Ashford, CO 80512<br>P: (970) 555-0182</p>
  </main>

  <footer class="footer">
    <div class="footer__item">
      <span class="footer__icon"><svg width="12" height="12" viewBox="0 0 24 24"><path fill="#fff" d="M6.6 10.8a15 15 0 0 0 6.6 6.6l2.2-2.2c.3-.3.7-.4 1-.2 1.1.4 2.3.6 3.6.6.6 0 1 .4 1 1V20c0 .6-.4 1-1 1A17 17 0 0 1 3 4c0-.6.4-1 1-1h3.5c.6 0 1 .4 1 1 0 1.3.2 2.5.6 3.6.1.3 0 .7-.2 1z"/></svg></span>
      <span>+62 11 5550 0142</span>
    </div>
    <div class="footer__item">
      <span class="footer__icon"><svg width="12" height="12" viewBox="0 0 24 24"><path fill="#fff" d="M2 5h20v14H2zm2 2v.5l8 5 8-5V7z"/></svg></span>
      <span>verdalyn.com</span>
    </div>
    <div class="footer__item">
      <span class="footer__icon"></span>
      <span>@verdalyn</span>
    </div>
  </footer>

  <div class="band band--bottom-left"></div>
  <div class="band band--bottom-right"></div>
</div>
</body>
</html>
```